WebDesign Flyer - A5 Double Sided

We create a complete web presence for local businesses.
A comprehensive background on our services and company can be found at www.brightnetstall.co.uk and on the attached sales document.

We want these flyers (a5, double sided, colour) to portray us as a local, professional and friendly service that will take care fully of a business's online presence. This includes website, hosting, email, domain AND IMPORTANTLY: we also can build them a business profile on business directory websites such as PinTown, OurCornerHub, Vistamap Spots, Quib etc. which helps them increase their profit.

Target Market(s)

Small to medium businesses found on the high street. eg: restaurants, physios, doctors, retail shops, salons, hairdressers, as well as more corporate businesses like accountancy firms and lawyers.

Industry/Entity Type

Business Directory

Requirements
Must have
• Full project files provided with all required elements if design is chosen. Design to mention: sites can be updated in less than 1 minute in 3 clicks, No contracts, money back guarantee (no risk), prices from £400, SEO as standard, brightnetstall.co.uk, 020 7946 0381, info@brightnetstall.co.uk, 10% discount with this flyer until December 20th 2010.
Nice to have
• To mention: dedicated support, business photos (see brightnetstall.co.uk/features), Chatterly, Peepline, ReelBox, Snapvault, CareerMesh Integration, free consultation, logos of services we provide (see logos.zip for examples).
Should not have
• our logo featured too prominently.

```html
<!DOCTYPE html>
<html lang="en">
<head>
<meta charset="utf-8">
<title>Bright Net Stall – A5 Flyer</title>
<link href="https://fonts.googleapis.com/css2?family=Caprasimo&display=swap" rel="stylesheet">
<style>
  :root {
    --sky: #3ec5f0;
    --sky-soft: #5ccdf3;
    --orange: #f7941d;
    --ink: #231f20;
    --white: #ffffff;
    --logo-blue: #1b9fd8;
  }
  html, body {
    margin: 0;
    padding: 0;
    width: 1200px;
    height: 851px;
    overflow: hidden;
    background: var(--sky);
  }
  .flyer {
    position: relative;
    width: 1200px;
    height: 851px;
    font-family: "Caprasimo", "Cooper Black", serif;
    color: var(--ink);
  }
  .page {
    position: absolute;
    top: 0;
    width: 600px;
    height: 851px;
    overflow: hidden;
    background: var(--sky);
  }
  .page--front { left: 0; }
  .page--back { left: 600px; }

  .backdrop {
    position: absolute;
    width: 640px;
    height: 640px;
    border-radius: 50%;
  }
  .page--front .backdrop {
    left: 200px;
    top: -110px;
    background: radial-gradient(circle, var(--sky-soft) 0%, var(--sky) 70%);
  }
  .page--back .backdrop {
    left: 140px;
    top: -150px;
    background: radial-gradient(circle, var(--sky-soft) 0%, var(--sky) 70%);
  }

  .swirl-art {
    position: absolute;
    left: 190px;
    top: 90px;
    width: 350px;
    height: 350px;
    border-radius: 50%;
    background: radial-gradient(circle at 50% 45%, rgba(255,255,255,0.55) 0%, rgba(255,255,255,0) 65%);
  }

  .callout {
    position: absolute;
    left: 150px;
    top: 142px;
    width: 280px;
    height: 178px;
    box-sizing: border-box;
    border: 9px solid var(--white);
    border-radius: 0 38px 0 38px;
    background: var(--orange);
    color: var(--white);
    text-align: center;
    font-size: 23px;
    line-height: 30px;
    padding-top: 18px;
  }
  .callout p { margin: 0 0 6px; }

  .headline {
    position: absolute;
    left: 160px;
    top: 336px;
    margin: 0;
    font-size: 44px;
    line-height: 56px;
    font-weight: 400;
    color: var(--ink);
    white-space: nowrap;
  }

  .benefits {
    position: absolute;
    left: 105px;
    top: 460px;
    margin: 0;
    padding: 0;
    list-style: none;
    color: var(--white);
    font-size: 20px;
    line-height: 26px;
    white-space: nowrap;
  }
  .benefits li {
    position: relative;
    padding-left: 35px;
    margin-bottom: 8px;
  }
  .benefits li::before {
    content: "";
    position: absolute;
    left: 0;
    top: 6px;
    width: 14px;
    height: 14px;
    border-radius: 50%;
    background: var(--white);
  }

  .brand-badge {
    position: absolute;
    left: 206px;
    top: 725px;
    width: 186px;
    height: 74px;
    box-sizing: border-box;
    border: 3px solid var(--logo-blue);
    border-radius: 12px;
    background: var(--white);
    display: flex;
    align-items: center;
    justify-content: center;
    gap: 7px;
    font-size: 16px;
    color: var(--logo-blue);
    white-space: nowrap;
  }
  .brand-badge__dot {
    width: 14px;
    height: 14px;
    border-radius: 50%;
    background: var(--logo-blue);
    flex: none;
  }

  .contact {
    position: absolute;
    left: 0;
    top: 808px;
    width: 600px;
    text-align: center;
    font-size: 14px;
    line-height: 17px;
    color: var(--ink);
  }
  .contact p { margin: 0; }
  .contact .gap { display: inline-block; width: 20px; }

  .pitch {
    position: absolute;
    left: 0;
    top: 98px;
    width: 600px;
    text-align: center;
    font-size: 19px;
    line-height: 24.5px;
    white-space: nowrap;
  }
  .pitch p { margin: 0 0 8px; }

  .offer {
    position: absolute;
    left: 0;
    top: 572px;
    width: 600px;
    text-align: center;
    color: var(--white);
    font-size: 25px;
    line-height: 32px;
    margin: 0;
    white-space: nowrap;
  }
</style>
</head>
<body>
<main class="flyer">

  <section class="page page--front">
    <div class="backdrop" role="img" aria-label="Soft pale blue concentric rings decoration"></div>
    <div class="swirl-art" role="img" aria-label="Decorative white swirl of circles and dots behind the question bubble"></div>

    <div class="callout">
      <p>Local company?</p>
      <p>Need a website?</p>
      <p>Don’t know<br>where to start?</p>
    </div>

    <h1 class="headline">We can help.</h1>

    <ul class="benefits">
      <li>Websites can be updated in less<br>than 1 minute in 3 clicks</li>
      <li>No contracts, money back<br>guarantee</li>
      <li>Prices from £400</li>
      <li>SEO as standard</li>
      <li>10% discount with this flyer<br>until December 20th 2010!</li>
    </ul>

    <div class="brand-badge"><span class="brand-badge__dot"></span>Bright Net Stall</div>

    <footer class="contact">
      <p>www.brightnetstall.co.uk<span class="gap"></span>020 7946 0381</p>
      <p>info@brightnetstall.co.uk</p>
    </footer>
  </section>

  <section class="page page--back">
    <div class="backdrop" role="img" aria-label="Soft pale blue concentric rings decoration"></div>

    <div class="pitch">
      <p>Do you want to boost your companies’ earnings<br>by increasing your online presence?</p>
      <p>Are you confused by the vast amount of social<br>media networks online?</p>
      <p>Do you want to tap into those valuable<br>markets, but just don’t know where to begin?</p>
      <p>Local company BRIGHTNETSTALL<br>are here to help!</p>
      <p>We can take care of your online presence,<br>including website, hosting, email and domain,<br>and can build you a business profile on business<br>directory sites such as PinTown,<br>OurCornerHub, Vistamap Spots, Quib etc.<br>which helps you increase your profits.</p>
      <p>Not only that, but we have Chatterly, Peepline,<br>ReelBox, Snapvault and CareerMesh integration -<br>all for no extra charge!</p>
    </div>

    <p class="offer">Prices start at £400 - what are you<br>waiting for?<br>Call us now on 020 7946 0381!</p>

    <div class="brand-badge"><span class="brand-badge__dot"></span>Bright Net Stall</div>

    <footer class="contact">
      <p>www.brightnetstall.co.uk<span class="gap"></span>020 7946 0381</p>
      <p>info@brightnetstall.co.uk</p>
    </footer>
  </section>

</main>
</body>
</html>
```